Re-design of website: www.velmarpromo.ca/en/

Velmar Promo is a promotional agency specializing in on-site marketing. We are re-designing their website.

We have already produced a prototype:
http://borquelab.com/velmarpromo_siteweb/

The architecture in the prototype must be respected. Please dress up the design with green, grey and black circles and other textures found on their current website www.velmarpromo.ca

Inspiration for design that we like, clean, flat design:

- http://www.tundrafolk.co/
- http://quillborough.com/#!/process
- http://wearedelvani.com/

Delivrables: PSD files of each page of the prototype

Here are the images of their print portfolio: http://ftp.velmarpromo.ca/clients/VMP/VELMARPROMO-PORTFOLIO-2012_EN.zip

Industry/Entity Type

Architecture

Requirements
Must have
• Responsive Design

```html
<!DOCTYPE html>
<html lang="fr">
<head>
<meta charset="utf-8">
<title>Velmar Promo — Agence 100 % promo</title>
<link rel="stylesheet" href="https://fonts.googleapis.com/css2?family=Arimo:wght@400;700&display=swap">
<style>
  :root{
    --green:#a0d26a;
    --green-dark:#5e8a3a;
    --charcoal:#3b3b3b;
    --ink:#2f2f2f;
    --paper:#f4f4f4;
    --mist-a:#e4e4e4;
    --mist-b:#f7f7f7;
    --white:#ffffff;
  }
  *{box-sizing:border-box;margin:0;padding:0}
  html,body{width:1074px;height:1200px;overflow:hidden}
  body{font-family:"Arimo",Arial,sans-serif;color:var(--ink);background:var(--paper);position:relative}
  a{color:inherit}

  .site-header{position:absolute;left:0;top:0;width:1074px;height:99px;background:var(--paper)}
  .brand{position:absolute;left:0;width:1074px;top:38px;display:flex;justify-content:center;align-items:center;gap:10px}
  .brand-name{font-size:36px;font-weight:700;letter-spacing:3px;color:#1e1e1e;text-transform:uppercase}
  .brand-dot{width:40px;height:40px;border-radius:50%;background:var(--green)}
  .lang-switch{position:absolute;left:868px;top:60px;font-size:14px;color:#333}

  .main-nav{position:absolute;left:0;top:99px;width:1074px;height:41px;background:var(--green)}
  .main-nav a{position:absolute;top:11px;font-size:17px;font-weight:700;text-decoration:none;color:var(--ink)}
  .social{position:absolute;top:7px;width:26px;height:26px;border-radius:50%;background:var(--charcoal)}

  .hero{position:absolute;left:0;top:140px;width:1074px;height:362px;background:var(--charcoal)}
  .video{position:absolute;left:149px;top:35px;width:379px;height:229px;border:3px solid #222;
    background:linear-gradient(135deg,#e9ece8 0%,#d7dcd5 40%,#2f6b33 60%,#e2e4e0 100%)}
  .video-bar{position:absolute;left:14px;right:14px;bottom:18px;height:24px;border-radius:3px;background:rgba(30,30,30,.85)}
  .video-bar .play{position:absolute;left:10px;top:6px;width:0;height:0;border-left:10px solid #fff;border-top:6px solid transparent;border-bottom:6px solid transparent}
  .video-bar .track{position:absolute;left:50px;right:60px;top:11px;height:3px;background:#777}
  .hero-title{position:absolute;left:592px;top:60px;font-size:30px;font-weight:400;color:var(--white)}
  .hero-text{position:absolute;left:592px;top:97px;width:325px;font-size:16.5px;line-height:17px;color:var(--white)}
  .btn{position:absolute;display:block;height:43px;border-radius:22px;background:var(--green);color:var(--white);
    font-size:17px;text-decoration:none;padding:11px 0 0 20px;box-shadow:0 3px 0 rgba(0,0,0,.15)}
  .btn .knob{position:absolute;right:7px;top:7px;width:29px;height:29px;border-radius:50%;background:var(--green-dark)}
  .btn .knob i{position:absolute;width:6px;height:6px;border-radius:50%;background:#2a2a2a}

  .services{position:absolute;left:0;top:502px;width:1074px;height:454px;background:linear-gradient(90deg,var(--mist-a),var(--mist-b) 60%,var(--mist-a));overflow:hidden}
  .deco{position:absolute;border-radius:50%;background:var(--green)}
  .tile{position:absolute;top:424px;width:150px;text-align:center}
  .tile-ring{width:142px;height:142px;margin:0 auto;border-radius:50%;padding:8px;
    background:linear-gradient(180deg,var(--green) 0 52%,var(--charcoal) 52% 100%)}
  .tile-photo{width:100%;height:100%;border-radius:50%}
  .tile-label{margin-top:14px;font-size:14.5px;line-height:15.5px;color:#333}

  .pitch-title{position:absolute;left:0;width:1074px;top:679px;text-align:center;font-size:47px;font-weight:700;color:var(--charcoal)}
  .pitch-text{position:absolute;left:182px;width:710px;top:735px;text-align:center;font-size:17.5px;line-height:19px;color:#333}

  .site-footer{position:absolute;left:0;top:956px;width:1074px;height:206px;background:var(--charcoal)}
  .foot-col{position:absolute;top:27px;width:200px;text-align:center;color:var(--white)}
  .foot-badge{width:86px;height:86px;margin:0 auto;border-radius:50%;background:var(--green);position:relative}
  .foot-badge::after{content:"";position:absolute;left:27px;top:27px;width:32px;height:32px;border-radius:50%;background:var(--charcoal)}
  .foot-col h3{margin-top:17px;font-size:15px;color:var(--green)}
  .foot-col p{margin-top:3px;font-size:11.5px;line-height:12.5px}
  .foot-col a{font-size:11.5px;color:var(--green)}
  .legal{position:absolute;left:0;top:1162px;width:1074px;height:38px;background:var(--green);text-align:center;font-size:10px;padding-top:13px;color:#333}
</style>
</head>
<body>
  <header class="site-header">
    <div class="brand"><span class="brand-name">Velmar Promo</span><span class="brand-dot"></span></div>
    <a class="lang-switch" href="#">English</a>
  </header>

  <nav class="main-nav">
    <a href="#" style="left:137px">Agence</a>
    <a href="#" style="left:217px">Services</a>
    <a href="#" style="left:301px">Réalisations</a>
    <a href="#" style="left:426px">Événements</a>
    <a href="#" style="left:545px">Recrutement</a>
    <a href="#" style="left:673px">Contact</a>
    <span class="social" style="left:775px"></span>
    <span class="social" style="left:815px"></span>
    <span class="social" style="left:856px"></span>
    <span class="social" style="left:897px"></span>
  </nav>

  <section class="hero">
    <div class="video" role="img" aria-label="Vidéo de présentation d'une campagne promotionnelle en points de vente">
      <div class="video-bar"><span class="play"></span><span class="track"></span></div>
    </div>
    <h1 class="hero-title">AGENCE 100 % PROMO</h1>
    <p class="hero-text">Lorem ipsum dolor sit amet, consectetur adipisicing elit, sed do eiusmod tempor mj incididunt consectetur adipisicing elit, sed do eiusmod tempor incididunt.</p>
    <a class="btn" href="#" style="left:592px;top:189px;width:171px">en savoir plus<span class="knob"><i style="left:7px;top:12px"></i><i style="left:15px;top:7px"></i><i style="left:15px;top:16px"></i></span></a>
  </section>

  <section class="services">
    <span class="deco" style="left:33px;top:33px;width:124px;height:124px"></span>
    <span class="deco" style="left:-59px;top:148px;width:118px;height:118px"></span>
  </section>

  <div class="tile" style="left:134px"><div class="tile-ring"><div class="tile-photo" role="img" aria-label="Kiosque promotionnel en magasin" style="background:radial-gradient(circle,#b38a4a,#5a3b22)"></div></div><p class="tile-label">Design et<br>construction<br>de kiosque</p></div>
  <div class="tile" style="left:295px"><div class="tile-ring"><div class="tile-photo" role="img" aria-label="Animation musicale lors d'un événement" style="background:radial-gradient(circle,#c9743a,#4a3428)"></div></div><p class="tile-label">Stylisme et<br>recherche<br>d'ambiance</p></div>
  <div class="tile" style="left:457px"><div class="tile-ring"><div class="tile-photo" role="img" aria-label="Roue de concours promotionnel" style="background:radial-gradient(circle,#d84b5a,#3a5fa8)"></div></div><p class="tile-label" style="margin-top:6px">Création de<br>mécanique<br>et gestion de<br>concours</p></div>
  <div class="tile" style="left:618px"><div class="tile-ring"><div class="tile-photo" role="img" aria-label="Montage de réseaux sociaux" style="background:radial-gradient(circle,#e9eef5,#6a8fc4)"></div></div><p class="tile-label">Campagnes<br>virales et<br>médias sociaux</p></div>
  <div class="tile" style="left:780px"><div class="tile-ring"><div class="tile-photo" role="img" aria-label="Poignée de main entre une main humaine et une main robotique" style="background:radial-gradient(circle,#f2f2f2,#b9bcc2)"></div></div><p class="tile-label" style="margin-top:12px">Intégration de<br>nouvelles<br>technologies</p></div>

  <h2 class="pitch-title">S'OCCUPER DE TOUT</h2>
  <p class="pitch-text">Intégrer tout ce qui touche le consommateur pour lui faire vivre une expérience unique<br>et captivante. Offrir un éventail complet de services clés en main; du concept au<br>terrain. Réaliser des promos percutantes qui produisent des résultats.<br>Et viser un seul objectif : vous démarquer et vous faire remarquer.</p>
  <a class="btn" href="#" style="left:447px;top:835px;width:172px">en savoir plus<span class="knob"><i style="left:7px;top:12px"></i><i style="left:15px;top:7px"></i><i style="left:15px;top:16px"></i></span></a>

  <footer class="site-footer">
    <div class="foot-col" style="left:150px">
      <div class="foot-badge" aria-hidden="true"></div>
      <h3>Contact</h3><p>Lorem ipsum dolor sit<br>amet, consectetur.</p><a href="#">Nous contacter.</a>
    </div>
    <div class="foot-col" style="left:426px">
      <div class="foot-badge" aria-hidden="true"></div>
      <h3>Recrutement</h3><p>Lorem ipsum dolor sit<br>amet, consectetur.</p><a href="#">Appliquer</a>
    </div>
    <div class="foot-col" style="left:704px">
      <div class="foot-badge" aria-hidden="true"></div>
      <h3>Suivez-nous</h3><p>Lorem ipsum dolor sit<br>amet, consectetur.</p><a href="#">/velmarpromo</a>
    </div>
  </footer>

  <div class="legal">Copyright 2013 Velmar Promo. Tous droits réservés.</div>
</body>
</html>
```